Consulting Company needs business card design

We need a business card design for a new consulting and business solutions company based in Alder Isles called Corvale Partners Limited. Looking for a double sided business card with one side only including the company logo thats attached and the other including contact information. Logo contains blue and turquoise colors and is fine to be on both sides of the card.
Contact Information for Business Card
Corvale Partners Limited
P.O. Box HM318
Kestrel Point KP 02
Alder Isles
Name: Marcus Pellegrin
Position: Director
Telephone: 1 441 733 4906
Email: mpellegrin@corvale.example
Website: www.corvale.example

```html
<!DOCTYPE html>
<html lang="en">
<head>
<meta charset="utf-8">
<title>Corvale Partners Limited – Business Card</title>
<link href="https://fonts.googleapis.com/css2?family=Lato:wght@300;400;700&display=swap" rel="stylesheet">
<style>
  :root {
    --page: #e6e7e9;
    --white: #ffffff;
    --teal: #1bafb2;
    --sky: #2ea9e0;
    --brand-blue: #2b8fd0;
    --ink-teal: #17a3a6;
    --card-shadow: 0 10px 28px rgba(0,0,0,0.18);
  }
  * { box-sizing: border-box; margin: 0; padding: 0; }
  html, body {
    width: 1200px; height: 1200px; overflow: hidden;
    background: var(--page);
    font-family: "Lato", Arial, sans-serif;
  }
  .canvas {
    width: 1200px; height: 1200px;
    display: flex; flex-direction: column; align-items: center; justify-content: center;
    gap: 64px;
  }
  .card {
    width: 900px; height: 514px;
    box-shadow: var(--card-shadow);
    position: relative; overflow: hidden;
  }

  /* Contact side */
  .card--contact { display: flex; background: var(--white); }
  .contact__brand-side {
    width: 48%; background: var(--white);
    position: relative;
  }
  .brand-mark {
    position: absolute; top: 46px; right: 28px;
    display: flex; align-items: center; gap: 12px;
  }
  .brand-mark__dot {
    width: 40px; height: 40px; border-radius: 50%;
    background: var(--sky);
  }
  .brand-mark__name {
    font-weight: 700; font-size: 40px; letter-spacing: 1px;
    color: var(--sky);
  }
  .address {
    position: absolute; left: 42px; bottom: 60px;
    font-style: normal;
    color: var(--brand-blue); font-size: 22px; line-height: 1.3;
  }
  .address__company {
    font-weight: 700; color: var(--ink-teal); font-size: 25px; margin-bottom: 6px;
  }
  .contact__info-side {
    flex: 1; background: var(--teal); color: var(--white);
    padding: 48px 40px 0 44px;
  }
  .name-box {
    border: 1.5px solid rgba(255,255,255,0.85);
    padding: 16px 20px 14px;
    margin-bottom: 78px;
  }
  .name-box__name {
    font-size: 34px; letter-spacing: 0.5px; text-transform: uppercase; font-weight: 300;
    white-space: nowrap;
  }
  .name-box__name strong { font-weight: 700; }
  .name-box__role { font-size: 18px; margin-top: 2px; }
  .contact-list { list-style: none; display: flex; flex-direction: column; gap: 18px; }
  .contact-list li { display: flex; align-items: center; gap: 14px; font-size: 23px; white-space: nowrap; }
  .contact-list svg { width: 24px; height: 24px; flex: none; }

  /* Logo side */
  .card--logo {
    background: var(--sky);
    display: flex; align-items: center; justify-content: center;
  }
  .card--logo .brand-mark { position: static; gap: 20px; }
  .card--logo .brand-mark__dot { width: 74px; height: 74px; background: var(--white); }
  .card--logo .brand-mark__name { font-size: 78px; color: var(--white); letter-spacing: 3px; }
</style>
</head>
<body>
<main class="canvas">
  <section class="card card--contact">
    <div class="contact__brand-side">
      <div class="brand-mark">
        <span class="brand-mark__dot"></span>
        <span class="brand-mark__name">CORVALE</span>
      </div>
      <address class="address">
        <div class="address__company">Corvale Partners Limited</div>
        <div>P.O. Box HM318</div>
        <div>Kestrel Point KP 02</div>
        <div>Alder Isles</div>
      </address>
    </div>
    <div class="contact__info-side">
      <div class="name-box">
        <div class="name-box__name"><strong>Marcus</strong> Pellegrin</div>
        <div class="name-box__role">Director</div>
      </div>
      <ul class="contact-list">
        <li>
          <svg viewBox="0 0 24 24" fill="none" stroke="#fff" stroke-width="1.6"><circle cx="12" cy="12" r="11"/><path d="M8.5 7c-.8.8-.9 2.2.4 4.2 1.5 2.3 3.5 4.2 5 4.9 1 .5 1.8.3 2.4-.3l-1.6-1.6-1.3.8c-1-.5-2.4-1.9-3-3l.8-1.3L9.6 7z"/></svg>
          1 441 733 4906
        </li>
        <li>
          <svg viewBox="0 0 24 24" fill="none" stroke="#fff" stroke-width="1.6"><circle cx="12" cy="12" r="11"/><rect x="6.5" y="8" width="11" height="8"/><path d="M6.5 8l5.5 4.5L17.5 8"/></svg>
          mpellegrin@corvale.example
        </li>
        <li>
          <svg viewBox="0 0 24 24" fill="none" stroke="#fff" stroke-width="1.6"><circle cx="12" cy="12" r="11"/><circle cx="12" cy="12" r="6"/><path d="M6 12h12M12 6c-2.5 3-2.5 9 0 12M12 6c2.5 3 2.5 9 0 12"/></svg>
          www.corvale.example
        </li>
      </ul>
    </div>
  </section>

  <section class="card card--logo">
    <div class="brand-mark">
      <span class="brand-mark__dot"></span>
      <span class="brand-mark__name">CORVALE</span>
    </div>
  </section>
</main>
</body>
</html>
```